Brindle School of Music Website Design

Brindle School of Music would like to have a website designed. They are a new business similar to Halvern (https://halvernmusic.example).

We prefer using Adobe Fonts throughout the design. Kepler was used for the logo. Lorem Ipsum is fine to use except for headers.

Please keep track of any images/icons that are used in your design. We plan on purchasing the images used in the winning design.

Target Market(s)

Children age 10 - 18

Number of Pages Required

1 page

Font styles to use
Sans Serif

Colors
0054AA
0677BA
7BADD7
CADEEF
E8F1F8

```html
<!DOCTYPE html>
<html lang="en">
<head>
<meta charset="utf-8">
<title>Brindle School of Music</title>
<link href="https://fonts.googleapis.com/css2?family=Noto+Serif:wght@600;700&family=Poppins:wght@400;500&display=swap" rel="stylesheet">
<style>
:root{
  --navy:#0f2a8a;
  --navy-deep:#0b1a4a;
  --royal:#0054AA;
  --ocean:#0677BA;
  --sky:#7BADD7;
  --mist:#CADEEF;
  --ice:#E8F1F8;
  --ink:#1b1f3a;
  --grey:#555a6e;
  --white:#ffffff;
  --serif:"Noto Serif", Georgia, serif;
  --sans:"Poppins", Arial, sans-serif;
}
*{box-sizing:border-box;margin:0;padding:0}
html,body{width:1200px;height:3904px;overflow:hidden}
body{position:relative;background:var(--white);font-family:var(--sans);color:var(--ink)}
.abs{position:absolute}
.btn{position:absolute;display:flex;align-items:center;justify-content:center;border-radius:6px;font-size:12px;text-transform:uppercase;background:var(--ocean);color:var(--white);font-family:var(--sans)}
.serif{font-family:var(--serif);font-weight:600}

/* top bar & nav */
.topbar{left:0;top:0;width:1200px;height:37px;background:var(--navy)}
.topbar .search{left:765px;top:0;width:240px;height:37px;border-left:1px solid #3a4fa6;border-right:1px solid #3a4fa6;color:#cfd6f0;font-size:12px;padding:10px 16px}
.topbar .account{left:1025px;top:9px;color:#fff;font-size:12px;display:flex;gap:8px;align-items:center}
.nav{left:0;top:37px;width:1200px;height:75px;background:#fff;box-shadow:0 2px 6px rgba(0,0,0,.08)}
.brand{left:58px;top:14px;color:var(--navy);font-family:var(--serif);font-weight:700;font-size:19px;line-height:22px;display:flex;gap:8px;align-items:center}
.brand i{display:block;width:14px;height:14px;border-radius:50%;background:var(--navy)}
.menu{left:287px;top:30px;display:flex;font-size:12px;text-transform:uppercase}
.menu span{margin-right:34px}
.nav .btn{left:990px;top:19px;width:142px;height:37px}

/* hero */
.hero{left:0;top:112px;width:1200px;height:638px;background:linear-gradient(110deg,#8a8f9c 0%,#5d6b80 45%,#2c5a7a 75%,#6d8aa0 100%)}
.hero h1{left:0;width:1200px;top:140px;text-align:center;color:#fff;font-family:var(--serif);font-weight:600;font-size:62px;line-height:76px}
.hero p{left:0;width:1200px;top:298px;text-align:center;color:#fff;font-size:13px;line-height:21px}
.donate-tab{left:0;top:378px;width:122px;height:38px;background:var(--ocean);color:#fff;font-size:12px;display:flex;align-items:center;justify-content:center;border-radius:0 6px 6px 0}

/* offer */
.offer{left:60px;top:556px;width:1079px;height:465px;background:var(--navy);border-radius:18px;overflow:hidden}
.offer .kicker{left:0;width:1079px;top:148px;text-align:center;color:#fff;font-size:12px}
.offer h2{left:0;width:1079px;top:172px;text-align:center;color:#fff;font-size:48px}
.offer p{left:270px;width:540px;top:232px;text-align:center;color:#fff;font-size:16px;line-height:24px}
.offer .btn.primary{left:389px;top:342px;width:143px;height:37px}
.offer .btn.ghost{left:548px;top:342px;width:143px;height:37px;background:#fff;color:var(--navy)}

/* section headings */
.heading{left:0;width:1200px;text-align:center;font-family:var(--serif);font-weight:600;font-size:42px;color:var(--ink)}
.heading em{font-style:normal;color:var(--navy)}

/* programs */
.card{top:1216px;width:252px;height:272px;background:#fff;border-radius:8px;box-shadow:0 2px 10px rgba(0,84,170,.18);overflow:hidden}
.card .photo{position:absolute;left:5px;top:5px;width:242px;height:168px;border-radius:4px}
.card h3{position:absolute;left:0;width:252px;top:190px;text-align:center;font-family:var(--serif);font-weight:600;font-size:15px;color:var(--navy)}
.card p{position:absolute;left:0;width:252px;top:218px;text-align:center;font-size:12px;color:var(--grey)}
.card-more{left:137px;top:1466px;width:97px;height:37px;text-transform:none;font-size:13px}
.arrow{width:34px;height:34px;border-radius:50%;top:1334px;display:flex;align-items:center;justify-content:center}
.arrow.prev{left:44px;background:#fff;border:2px solid var(--ocean)}
.arrow.next{left:1122px;background:var(--ocean)}

/* about */
.about{left:0;top:1586px;width:1200px;height:550px;background:linear-gradient(100deg,#1c2746 0%,#222d52 55%,#1a2240 100%)}
.about .accent{left:60px;top:78px;width:240px;height:170px;background:var(--royal);border-radius:10px 0 0 0}
.about .photo{left:80px;top:99px;width:420px;height:374px;border-radius:14px;background:linear-gradient(135deg,#8a5a3a,#b8483e 40%,#3f3b52 75%,#6a5a48)}
.about h2{left:611px;top:120px;width:560px;color:#fff;font-size:42px;line-height:58px}
.about p{left:609px;top:240px;width:480px;color:#fff;font-size:12.5px;line-height:21px}
.about .btn{left:609px;top:370px;width:120px;height:36px}

/* stats */
.stats{left:0;top:2136px;width:1200px;height:361px;background:var(--ocean)}
.stats .heading{top:105px;color:#fff}
.stat{top:180px;width:276px;text-align:center;color:#fff}
.stat svg{display:block;margin:0 auto}
.stat strong{display:block;margin-top:10px;font-family:var(--serif);font-weight:600;font-size:35px;line-height:42px}
.stat span{display:block;font-size:14px;line-height:21px;font-weight:500;margin-top:6px}

/* courses */
.course{top:2718px;width:210px;text-align:center}
.course .circle{width:90px;height:90px;border-radius:50%;margin:0 auto;background:var(--mist);box-shadow:0 3px 6px rgba(0,0,0,.15);display:flex;align-items:center;justify-content:center}
.course .circle.active{background:var(--royal);border:3px solid var(--ocean)}
.course h3{margin-top:20px;font-family:var(--serif);font-weight:600;font-size:15px;color:var(--navy)}
.course p{margin-top:8px;font-size:12px;line-height:21px;color:var(--grey)}

/* gift */
.gift{left:60px;top:2972px;width:1079px;height:464px;background:var(--ice);border-radius:20px;overflow:hidden}
.gift .halo{left:592px;top:78px;width:560px;height:560px;border-radius:50%;background:var(--royal)}
.gift .portrait{left:610px;top:10px;width:440px;height:454px;border-radius:200px 200px 0 0;background:linear-gradient(180deg,#4a2e22 0%,#a06a48 35%,#efe3a0 70%,#f3e7ad 100%)}
.gift h2{left:43px;top:140px;font-size:42px;color:var(--ink)}
.gift h2 em{font-style:normal;color:var(--navy)}
.gift p{left:45px;top:214px;width:470px;font-size:16.5px;line-height:24px;color:var(--ink)}
.gift .cite{left:45px;top:296px;font-family:var(--serif);font-weight:600;font-size:14px;color:var(--ocean)}
.gift .btn{left:45px;top:342px;width:138px;height:37px}

/* footer */
.footer{left:0;top:3512px;width:1200px;height:354px;background:var(--navy-deep);color:#fff}
.footer .name{left:58px;top:120px;width:250px;text-align:center;font-family:var(--serif);font-weight:700;font-size:44px;line-height:52px;display:flex;flex-direction:column;align-items:center}
.footer .name i{display:block;width:60px;height:60px;border-radius:50%;background:var(--royal);margin-bottom:14px}
.footer .name small{font-size:20px;font-weight:700;line-height:26px}
.footer h4{font-family:var(--serif);font-weight:600;font-size:14px;color:var(--sky)}
.footer .col{top:88px}
.footer .links span{display:block;font-size:11.5px;margin-bottom:20px;text-transform:uppercase}
.footer .contact div{display:flex;gap:12px;font-size:12.5px;line-height:20px;margin-bottom:14px}
.footer .email{left:888px;top:124px;width:252px;height:33px;background:#fff;border-radius:6px;color:#333;font-size:12px;padding:8px 16px}
.footer .btn{left:888px;top:174px;width:96px;height:32px;text-transform:none;font-size:12px}
.copy{left:0;top:3866px;width:1200px;height:38px;background:var(--ocean);color:#fff;font-size:11px;display:flex;align-items:center;justify-content:center}
</style>
</head>
<body>

<div class="abs topbar">
  <div class="abs search">Search...</div>
  <div class="abs account">
    <svg width="16" height="16" viewBox="0 0 16 16"><circle cx="8" cy="8" r="7" fill="none" stroke="#fff" stroke-width="1.2"/><circle cx="8" cy="6.5" r="2.3" fill="none" stroke="#fff" stroke-width="1.2"/><path d="M3.5 12.5c1.5-2 7.5-2 9 0" fill="none" stroke="#fff" stroke-width="1.2"/></svg>
    My Account
  </div>
</div>

<header class="abs nav">
  <div class="abs brand"><i></i><span>BRINDLE<br>School of Music</span></div>
  <nav class="abs menu"><span>Our Programs</span><span>About Us</span><span>Our Impact</span><span>Support Brindle</span><span>Support Brindle</span></nav>
  <div class="btn">Register Online</div>
</header>

<section class="abs hero" role="img" aria-label="Photo of young singers performing at microphones in a studio">
  <h1 class="abs">Learn The Music<br>From The Masters</h1>
  <p class="abs">Lorem Ipsum is simply dummy text of the printing and typesetting industry.<br>Lorem Ipsum has been the industry's standard dummy text.</p>
  <div class="abs donate-tab">DONATE NOW</div>
</section>

<section class="abs offer">
  <svg class="abs" style="left:0;top:0" width="1079" height="465">
    <circle cx="-10" cy="-10" r="360" fill="#0677BA"/>
    <circle cx="1079" cy="465" r="130" fill="#0677BA"/>
    <g fill="none" stroke="#7BADD7" stroke-width="2.5">
      <polygon points="180,90 185,101 197,102 188,110 191,122 180,116 169,122 172,110 163,102 175,101"/>
      <polygon points="208,375 213,386 225,387 216,395 219,407 208,401 197,407 200,395 191,387 203,386"/>
      <polygon points="888,283 893,294 905,295 896,303 899,315 888,309 877,315 880,303 871,295 883,294"/>
      <path d="M928 120v-18l18-5v18M928 120a5 5 0 1 1-1-1M946 115a5 5 0 1 1-1-1"/>
      <path d="M82 262v-18l18-5v18M82 262a5 5 0 1 1-1-1M100 257a5 5 0 1 1-1-1"/>
    </g>
  </svg>
  <div class="abs kicker">Opening Offer</div>
  <h2 class="abs serif">GET A FREE LESSON</h2>
  <p class="abs">Lorem Ipsum is simply dummy text of the printing and typesetting industry. Lorem Ipsum has been the industry's standard dummy text.</p>
  <div class="btn primary">Register Online</div>
  <div class="btn ghost">Choose Class</div>
</section>

<h2 class="abs heading" style="top:1140px">OUR <em>PROGRAMES</em></h2>

<div class="abs card" style="left:60px"><div class="photo" role="img" aria-label="Photo of a child playing guitar in a colourful classroom" style="background:linear-gradient(135deg,#d9a04a,#8b5a3a 50%,#c8c0b0)"></div><h3>Early Childhood</h3><p>Newborns – 8 years</p></div>
<div class="abs card" style="left:333px"><div class="photo" role="img" aria-label="Photo of a teacher giving a private guitar lesson" style="background:linear-gradient(135deg,#d8d2c8,#8a6a50 55%,#5a4a40)"></div><h3>Private Lessons</h3><p>Ages 4+</p></div>
<div class="abs card" style="left:610px"><div class="photo" role="img" aria-label="Photo of children sitting in a circle during a group class" style="background:linear-gradient(135deg,#e8e4dc,#c8bfb0 50%,#a04038)"></div><h3>Group Classes</h3><p>Ages 6+</p></div>
<div class="abs card" style="left:887px"><div class="photo" role="img" aria-label="Photo of a teacher and child at a keyboard" style="background:linear-gradient(135deg,#b8b4b0,#f0ece8 50%,#3a3a3a)"></div><h3>Summer Camps</h3><p>All Ages. By Experience.</p></div>
<div class="btn card-more">More Info</div>
<div class="abs arrow prev"><svg width="16" height="12"><path d="M15 6H2M6 1L1 6l5 5" fill="none" stroke="#1b1f3a" stroke-width="1.8"/></svg></div>
<div class="abs arrow next"><svg width="16" height="12"><path d="M1 6h13M10 1l5 5-5 5" fill="none" stroke="#fff" stroke-width="1.8"/></svg></div>

<section class="abs about" role="img" aria-label="Dim background photo of a singer at a microphone">
  <div class="abs accent"></div>
  <div class="abs photo" role="img" aria-label="Photo of a teacher and a young student holding a ukulele"></div>
  <h2 class="abs serif">ABOUT BRINDLE SCHOOL<br>OF MUSIC</h2>
  <p class="abs">Lorem Ipsum is simply dummy text of the printing and typesetting industry. Lorem Ipsum has been the industry's standard dummy text ever since the 1500s, when an unknown printer took a galley of type and scrambled it to make a type specimen book. It has survived not only five centuries, but also the leap into electronic typesetting, remaining essentially unchanged.</p>
  <div class="btn">Learn More</div>
</section>

<section class="abs stats">
  <h2 class="abs heading">2000+ STUDENTS ANNUALY</h2>
  <div class="abs stat" style="left:46px">
    <svg width="50" height="50" viewBox="0 0 50 50" fill="none" stroke="#fff" stroke-width="2"><path d="M18 6h14l-4 8h-6z"/><path d="M20 14C8 20 6 42 25 44c12 0 16-8 15-16"/><text x="16" y="36" fill="#fff" stroke="none" font-size="16" font-family="Arial">$</text><circle cx="37" cy="34" r="7"/><path d="M34 34l2 2 4-4"/></svg>
    <strong>$1.5 Million</strong><span>Lorem Ipsum is simply<br>dummy text.</span></div>
  <div class="abs stat" style="left:322px">
    <svg width="50" height="50" viewBox="0 0 50 50" fill="none" stroke="#fff" stroke-width="2"><path d="M6 22L25 6l19 16"/><path d="M10 20v24h30V20"/><path d="M20 44V30h10v14"/><circle cx="25" cy="18" r="4"/></svg>
    <strong>25</strong><span>Lorem Ipsum is simply<br>dummy text.</span></div>
  <div class="abs stat" style="left:598px">
    <svg width="50" height="50" viewBox="0 0 50 50" fill="none" stroke="#fff" stroke-width="2"><path d="M3 18l22-9 22 9-22 9z"/><path d="M12 22v10c6 6 20 6 26 0V22"/><path d="M44 19v16"/></svg>
    <strong>100%</strong><span>Lorem Ipsum is simply<br>dummy text.</span></div>
  <div class="abs stat" style="left:874px">
    <svg width="50" height="50" viewBox="0 0 50 50" fill="none" stroke="#fff" stroke-width="2"><path d="M8 8l34 34M42 8L8 42"/><circle cx="16" cy="34" r="6"/><circle cx="34" cy="34" r="6"/></svg>
    <strong>70%</strong><span>Lorem Ipsum is simply<br>dummy text.</span></div>
</section>

<h2 class="abs heading" style="top:2634px">MUSIC <em>COURCES</em></h2>

<div class="abs course" style="left:60px"><div class="circle"><svg width="44" height="44" viewBox="0 0 44 44" fill="none" stroke="#0f2a8a" stroke-width="1.8"><ellipse cx="22" cy="24" rx="10" ry="4"/><path d="M12 24v10c0 4 20 4 20 0V24"/><ellipse cx="9" cy="14" rx="6" ry="2"/><ellipse cx="35" cy="14" rx="6" ry="2"/><path d="M9 16v24M35 16v24"/></svg></div><h3>Band</h3><p>Lorem Ipsum is simply dummy text of the printing.</p></div>
<div class="abs course" style="left:282px"><div class="circle"><svg width="44" height="44" viewBox="0 0 44 44" fill="none" stroke="#0f2a8a" stroke-width="1.8"><path d="M34 6L20 22"/><path d="M18 20c-6 0-12 6-10 12 2 6 10 6 14 2 4-4 2-10-4-14z"/><circle cx="16" cy="29" r="2.5"/><path d="M32 4l6 6"/></svg></div><h3>Guitar</h3><p>Lorem Ipsum is simply dummy text of the printing.</p></div>
<div class="abs course" style="left:497px"><div class="circle active"><svg width="44" height="44" viewBox="0 0 44 44" fill="none" stroke="#fff" stroke-width="2"><rect x="6" y="8" width="32" height="28" rx="4"/><path d="M15 8v28M22 8v28M29 8v28"/><path d="M15 8v14M22 8v14M29 8v14" stroke-width="5"/></svg></div><h3>Piano</h3><p>Lorem Ipsum is simply dummy text of the printing.</p></div>
<div class="abs course" style="left:715px"><div class="circle"><svg width="44" height="44" viewBox="0 0 44 44" fill="none" stroke="#0f2a8a" stroke-width="1.8"><path d="M12 38V12c0-4 20-4 20 0v26"/><path d="M8 38h28"/><path d="M17 12v26M22 11v27M27 12v26"/></svg></div><h3>Strings &amp; Orchestra</h3><p>Lorem Ipsum is simply dummy text of the printing.</p></div>
<div class="abs course" style="left:933px"><div class="circle"><svg width="44" height="44" viewBox="0 0 44 44" fill="none" stroke="#0f2a8a" stroke-width="1.8"><rect x="22" y="6" width="10" height="16" rx="5"/><path d="M27 22v6l-10 10"/><path d="M8 20v14M8 20l8-3v14"/><circle cx="6" cy="34" r="2.5"/><circle cx="14" cy="31" r="2.5"/></svg></div><h3>Voice &amp; Choir</h3><p>Lorem Ipsum is simply dummy text of the printing.</p></div>

<section class="abs gift">
  <div class="abs halo"></div>
  <div class="abs portrait" role="img" aria-label="Photo of a smiling girl in a yellow dress singing into a microphone"></div>
  <h2 class="abs serif">GIVE THE <em>GIFT OF MUSIC</em></h2>
  <p class="abs">“Lorem Ipsum is simply dummy text of the printing and typesetting industry. Lorem Ipsum has been the industry's standard dummy text.”</p>
  <div class="abs cite">Lorem ipsum is a dummy text.</div>
  <div class="btn">Donate Today</div>
</section>

<footer class="abs footer">
  <div class="abs name"><i></i>BRINDLE<small>SCHOOL OF MUSIC</small></div>
  <div class="abs col links" style="left:338px"><h4 style="margin-bottom:18px">Site Map</h4><span>Our Programs</span><span>About Us</span><span>Our Impact</span><span>Support Brindle</span><span>Support Brindle</span></div>
  <div class="abs col contact" style="left:615px;width:250px"><h4 style="margin-bottom:16px">Contact Us</h4>
    <div><svg width="16" height="20" viewBox="0 0 16 20" fill="none" stroke="#fff" stroke-width="1.4"><path d="M8 19s6-6 6-11A6 6 0 0 0 2 8c0 5 6 11 6 11z"/><circle cx="8" cy="8" r="2"/></svg><span>Lorem Ipsum is simply dummy<br>text of the printing.</span></div>
    <div><svg width="16" height="16" viewBox="0 0 16 16" fill="none" stroke="#fff" stroke-width="1.4"><path d="M3 1l3 3-2 2c1 2 3 4 5 5l2-2 3 3-2 3C6 14 2 10 1 3z"/></svg><span>(555) 014 2290</span></div>
    <div><svg width="16" height="14" viewBox="0 0 16 14" fill="none" stroke="#fff" stroke-width="1.4"><rect x="1" y="2" width="14" height="10"/><path d="M1 2l7 6 7-6"/></svg><span>info@brindlemusic.example</span></div>
  </div>
  <div class="abs col" style="left:888px"><h4>Subscribe To Our Newslatter</h4></div>
  <div class="abs email">E-mail</div>
  <div class="btn">Subscribe</div>
</footer>
<div class="abs copy">©2023 BRINDLE SCHOOL OF MUSIC .All rights reserved.</div>

</body>
</html>
```